Web Design Project (Mente Lumo)

We are going to do a therapy template to a psychologist. The site already exists, adress: www.mentelumo.net. So, its a total redesign job. I'm from Brazil, the language is PT-BR, so I'm gonna translate what you think be necessary. You can use the current structure from the website as a base to the new design. Check this template to see what I usually like: http://www.layoutkiosk.example/demo/51937.html
Updates

I'm waiting for new creative designs. The 'structure' image is just for 'pb'.

Requirements
Must have
• We need a modern menu, it should use a cool font style and make some kind of effect and little noise when the user pass over with the mouse (FLASH/HTML 5). The main page must emphasize the fact that we offer online treatment, like a picture or frame saying "Online Treatment, click here". It must also show the therapist picture and her name. The colors need to pass a tranquility feeling. The clinic telephone must always be present, doesn't matter which page the user is. The website must adapt to any resolution above 1024x768, crossbrowsing and accept javascript (I'll use www.agendrix.example, so its necessary embed code)
Nice to have
• I would appreciate if there was some kind of slow background animation, passing behind the text using the transparency.
Should not have
• Can't take too long to load, and won't have news or blog

```html
<!DOCTYPE html>
<html lang="pt-BR">
<head>
<meta charset="utf-8">
<title>Mente Lumo — Terapia Cognitiva</title>
<link href="https://fonts.googleapis.com/css2?family=Ubuntu:wght@400;500;700&family=Arimo:wght@400;700&display=swap" rel="stylesheet">
<style>
:root{
  --teal:#7fc9d3;
  --teal-dark:#3d8e98;
  --teal-text:#3f9aa0;
  --green:#7fb52f;
  --green-dark:#5e8f1c;
  --green-light:#b4d98a;
  --ink:#111;
  --navy:#1b2c5a;
  --white:#fff;
}
*{margin:0;padding:0;box-sizing:border-box}
html,body{width:1200px;height:836px;overflow:hidden}
body{position:relative;font-family:"Arimo",Arial,sans-serif;
  background:repeating-linear-gradient(135deg,#d3e9f3 0 2px,#dff0f7 2px 5px);}
.topline{position:absolute;left:0;top:0;width:1200px;height:6px;background:#111}
.header{position:absolute;left:0;top:6px;width:1200px;height:91px;
  background:linear-gradient(#8fd2da,#79c3cc 40%,#5ea9b2);border-bottom:2px solid #2f7b84}
.logo{position:absolute;left:181px;top:0;width:179px;height:122px;background:#050505;
  border:3px solid #c9d9dc;border-top:none;border-radius:0 0 12px 12px;
  display:flex;align-items:center;justify-content:center;gap:8px;z-index:2}
.logo-dot{width:14px;height:14px;border-radius:50%;background:var(--green-light)}
.logo-name{font-family:"Ubuntu",sans-serif;font-weight:700;font-size:22px;color:#cfe0d8}
.follow{position:absolute;right:142px;top:16px;display:flex;align-items:center;gap:6px;
  font-family:"Ubuntu",sans-serif;font-weight:700;font-size:12px;color:var(--white)}
.follow .sq{width:16px;height:16px;border-radius:3px;background:#2f7fb5}
.nav{position:absolute;right:142px;top:56px;display:flex;align-items:center;
  font-family:"Ubuntu",sans-serif;font-weight:700;font-size:15px;color:var(--white)}
.nav span{padding:0 17px;border-left:1px solid rgba(255,255,255,.35);line-height:14px}
.nav span:last-child{padding-right:0}
.nav span:first-child{border:1px solid #7c9c8f;background:#b7cfc0;color:#111;border-radius:5px;
  padding:4px 16px;line-height:17px;margin-right:10px}
.hero-title{position:absolute;left:162px;top:184px;font-family:"Ubuntu",sans-serif;font-weight:500;
  font-size:24px;color:var(--teal-dark);white-space:nowrap;letter-spacing:-.3px}
.hero-title b{font-weight:500;font-size:29px;color:var(--green)}
.hero-text{position:absolute;left:178px;top:226px;width:358px;text-align:center;
  font-weight:700;font-size:11.5px;line-height:16px;color:var(--teal-text)}
.btn-online{position:absolute;left:236px;top:358px;width:237px;height:53px;border-radius:10px;
  background:linear-gradient(#9ccf48,#5c8f1e);display:flex;align-items:center;padding-left:16px;
  font-family:"Ubuntu",sans-serif;font-weight:700;font-size:19px;letter-spacing:-.3px;color:var(--white)}
.btn-online .arrow{position:absolute;right:16px;top:14px;width:24px;height:24px;border-radius:50%;
  background:#3e6a12;display:flex;align-items:center;justify-content:center}
.deco{position:absolute;border-radius:16px}
.frame{position:absolute;left:677px;top:118px;width:352px;height:333px;border-radius:16px;
  border:3px solid #cfe8a8;background:#000;overflow:hidden;box-shadow:0 8px 14px rgba(0,0,0,.35)}
.frame .art{position:absolute;inset:0;background:radial-gradient(circle at 55% 40%,#4f86c4,#173a6a 55%,#000 85%)}
.frame .cap{position:absolute;left:40px;top:250px;font-family:"Ubuntu",sans-serif;line-height:1;color:var(--teal)}
.cap .v{font-size:28px}
.cap .s{font-size:15px;color:var(--green)}
.cap .p{display:block;margin-left:68px;font-size:32px;color:#2f6fe0}
.panel{position:absolute;left:132px;top:488px;width:676px;height:217px;background:var(--white);
  border:1px solid #c8d4d8;border-radius:12px}
.portrait{position:absolute;left:23px;top:17px;width:144px;height:151px;border:2px solid var(--green-light);
  background:linear-gradient(#9a9a9a,#555)}
.portrait-cap{position:absolute;left:26px;top:174px;font-family:"Ubuntu",sans-serif;font-size:12px;line-height:17px;color:var(--ink);white-space:nowrap}
.h2{font-family:"Ubuntu",sans-serif;font-weight:400;font-size:26px;color:var(--ink);white-space:nowrap}
.h2 em{font-style:normal;color:var(--green)}
.who{position:absolute;left:176px;top:18px}
.sub{font-family:"Ubuntu",sans-serif;font-weight:500;font-size:20px;color:var(--teal-text);margin-top:-4px}
.body{font-size:9.5px;line-height:14.5px;color:var(--ink)}
.who .body{width:184px;margin-top:2px}
.divider{position:absolute;left:390px;top:34px;width:2px;height:150px;background:#999}
.us{position:absolute;left:426px;top:18px}
.us .body{width:230px;margin-top:4px}
.side{position:absolute;left:819px;width:249px;height:70px;border-radius:4px;border:1px solid #a9b7bd;overflow:hidden}
.phone{top:488px;background:#cfe6f1}
.phone svg.tel{position:absolute;left:14px;top:6px}
.phone .feel{position:absolute;left:10px;top:54px;font-size:9px;color:var(--ink)}
.phone ul{position:absolute;right:10px;top:8px;list-style:none;font-family:"Ubuntu",sans-serif;font-size:13px;line-height:18px;color:var(--ink)}
.phone li{display:flex;align-items:center;gap:8px}
.ic{display:inline-block;width:12px;text-align:center;font-size:11px}
.ic-mob{display:inline-block;width:7px;height:11px;border:2px solid #222;border-radius:1px;margin:0 2px 0 3px}
.online{top:562px;background:var(--green)}
.online .fig{position:absolute;left:18px;top:8px;width:64px;height:56px;border-radius:8px;background:linear-gradient(#e7a24a,#3d7fc6)}
.online p{position:absolute;right:12px;top:4px;text-align:right;font-family:"Ubuntu",sans-serif;font-weight:500;font-size:29px;line-height:28px;color:var(--white)}
.map{top:636px;background:linear-gradient(#e3ecef,#c9d8de)}
.map p{position:absolute;left:20px;top:6px;font-family:"Ubuntu",sans-serif;color:var(--navy);font-size:22px;line-height:28px}
.map b{font-weight:500;font-size:30px}
.map .on{padding-left:94px}
.footer{position:absolute;left:0;top:723px;width:1200px;height:113px;background:#000;border-top:3px solid #4c9ea6}
.footer p{position:absolute;right:134px;top:19px;text-align:right;font-family:"Ubuntu",sans-serif;font-size:13px;line-height:18.5px;color:var(--white)}
</style>
</head>
<body>
<div class="topline"></div>
<header class="header">
  <div class="follow">Follow Us On : <i class="sq"></i><i class="sq"></i><i class="sq"></i></div>
  <nav class="nav"><span>Home</span><span>Tratamentos</span><span>Perguntas</span><span>Consultono</span><span>Localizacao</span><span>Contato</span></nav>
</header>
<div class="logo"><i class="logo-dot"></i><span class="logo-name">Mente Lumo</span></div>

<h1 class="hero-title">O Que e <b>Terapia Cognitiva?</b></h1>
<p class="hero-text">A Terapia Cognitiva tem como método a interpretação de processos e conteúdos mentais (as cognições), e sua influência na vida cotidiana. O comportamento e a emoção vêm depois do processamento cognitivo. É vital conhecermos nossos pensamentos para termos controle sobre eles, e assim podemos: nutri-los, expandi-los, reduzi-los ou rejeitá-los.</p>
<div class="btn-online">Online Treatment<i class="arrow"><svg width="10" height="10" viewBox="0 0 10 10" aria-hidden="true"><path d="M3 1 L7 5 L3 9" stroke="#fff" stroke-width="2" fill="none"/></svg></i></div>

<div class="deco" style="left:600px;top:112px;width:82px;height:78px;background:#8799a3"></div>
<div class="deco" style="left:553px;top:191px;width:46px;height:44px;background:#7fc9d3;border-radius:10px"></div>
<div class="deco" style="left:610px;top:199px;width:23px;height:21px;background:#b4d98a;border-radius:5px"></div>
<div class="deco" style="left:635px;top:219px;width:60px;height:78px;background:#b4d98a"></div>
<div class="deco" style="left:975px;top:112px;width:83px;height:78px;background:#7fc9d3"></div>
<div class="deco" style="left:1010px;top:219px;width:83px;height:78px;background:#7fc9d3"></div>
<div class="frame">
  <div class="art" role="img" aria-label="Ilustração de uma cabeça humana de perfil com engrenagens no cérebro"></div>
  <div class="cap"><span class="v">É vital</span> <span class="s">para saber seus</span><span class="p">pensamentos ...</span></div>
</div>

<section class="panel">
  <div class="portrait" role="img" aria-label="Foto da psicóloga Helena Duarte"></div>
  <p class="portrait-cap">Psicóloga Helena Duarte<br>CRP: 6/204518</p>
  <div class="who">
    <h2 class="h2">Who <em>Am I</em>?</h2>
    <h3 class="sub">Perfil</h3>
    <p class="body">At vero eos et accusamus et iusto odio dignissimos ducimus qui blanditiis praesentium voluptatum deleniti atque corrupti quos dolores et quas molestias excepturi sint occaecati cupiditate non provident, similique sunt in culpa qui officia deserunt mollitia animAi, id est laborum et dolorum fuga.</p>
  </div>
  <div class="divider"></div>
  <div class="us">
    <h2 class="h2">Quem <em>Somos?</em></h2>
    <p class="body">At vero eos et accusamus et iusto odio dignissimos ducimus qui blanditiis praesentium voluptatum deleniti atque corrupti quos dolores et quas molestias excepturi sint occaecati cupiditate non provident, similique sunt in culpa qui officia deserunt mollitia animAi, id est laborum et dolorum fuga.At vero eos et accusamus et iusto odio dignissimos ducimus qui blanditiis praesentium voluptatum deleniti atque.</p>
  </div>
</section>

<aside class="side phone">
  <svg class="tel" width="60" height="44" viewBox="0 0 60 44" aria-hidden="true">
    <path d="M4 14 Q30 0 56 14 L52 20 L42 17 L40 11 Q30 8 20 11 L18 17 L8 20 Z" fill="#111"/>
    <path d="M16 24 L44 24 L50 42 L10 42 Z" fill="#222"/>
    <circle cx="30" cy="33" r="5" fill="#666"/>
  </svg>
  <span class="feel">Feel Free To Call Us</span>
  <ul>
    <li><span class="ic">☎</span>(11) 3520-4170</li>
    <li><span class="ic"><i class="ic-mob"></i></span>(11) 9381-2054</li>
    <li><span class="ic"><i class="ic-mob"></i></span>(11) 7614-3308</li>
  </ul>
</aside>
<aside class="side online">
  <div class="fig" role="img" aria-label="Ilustração de atendente com fone e globo"></div>
  <p>Online<br>Treatment</p>
</aside>
<aside class="side map" role="img" aria-label="Mapa-múndi ao fundo do botão de localização">
  <p>Our <b>Location</b><br><span class="on">On <b>Map</b></span></p>
</aside>

<footer class="footer">
  <p>Rua das Acácias, 412, 5º andar, Sala 21 - Centro - Santo André, SP<br>Clique aqui para ver o mapa<br>contato@mentelumo.net<br>Copyright © 2012 - Todos os direitos reservados</p>
</footer>
</body>
</html>
```